Elmcrest Tutoring & Test Preparation
stationery and business card
Elmcrest Tutoring & Test Preparation - Education
Creative Brief
Simple
Doreen Falk
Director
Elmcrest Tutoring & Test Prep 245 Marlowe Park Rd, 3-B Fairlow, NJ 08921
dfalk@elmcresttutors.com
www.elmcresttutors.com
Elmcrest is a premier tutoring and test prep firm, and we focus on grades 7 - 12, college counseling
a quick list of tutoring services -- "Entrance Exam Prep, SAT Subject Tests, Academic Tutoring, Reading and Study Skills, College Counseling"

```html
<!DOCTYPE html>
<html lang="en">
<head>
<meta charset="utf-8">
<title>Elmcrest Tutoring &amp; Test Preparation — Stationery</title>
<link rel="stylesheet" href="https://fonts.googleapis.com/css2?family=Cinzel:wght@600&family=Open+Sans:wght@400;600&display=swap">
<style>
  :root{
    --stage:#2b2c2f;
    --stage-dark:#1f2022;
    --paper:#ffffff;
    --navy:#0c1f66;
    --blue:#1f4fc4;
    --blue-light:#4a7de6;
    --mark-faint:#e4e8f0;
    --ink:#2a2f3a;
    --caption:#8d9098;
  }
  *{box-sizing:border-box;margin:0;padding:0}
  html,body{width:1200px;height:317px;overflow:hidden}
  body{
    position:relative;
    background:radial-gradient(ellipse at 50% 40%, var(--stage) 0%, var(--stage-dark) 100%);
    font-family:"Open Sans", Arial, sans-serif;
    color:var(--ink);
  }
  .piece{position:absolute;background:var(--paper);box-shadow:0 2px 6px rgba(0,0,0,.45)}
  .clip{position:absolute;inset:0;overflow:hidden}
  .caption{position:absolute;font-size:5px;line-height:6px;color:var(--caption);text-align:center;width:100%;left:0;bottom:-9px}
  .wordmark{font-family:"Cinzel", Georgia, serif;font-weight:600;color:var(--navy);letter-spacing:.5px;white-space:nowrap}
  .dot{display:inline-block;border-radius:50%;background:var(--blue);vertical-align:middle}
  .blue-fill{background:linear-gradient(135deg,var(--blue-light) 0%,var(--blue) 45%,var(--navy) 100%)}
  .faint-mark{position:absolute;border-radius:50%;background:var(--mark-faint)}
  .tiny{font-size:3.5px;line-height:5px;color:var(--ink);white-space:nowrap}

  /* presentation logo */
  .brand-block{position:absolute;left:40px;top:14px;width:150px;text-align:center}
  .brand-block .dot{width:36px;height:36px;background:radial-gradient(circle at 35% 35%,var(--blue-light),var(--navy))}
  .brand-block .wordmark{display:block;font-size:17px;color:#ffffff;margin-top:6px}
  .brand-block .tagline{display:block;font-family:"Cinzel", Georgia, serif;font-size:5.5px;color:#cfd6e8;letter-spacing:1px;margin-top:1px}
  .brand-block .concept{display:block;font-size:5px;color:var(--caption);margin-top:5px}

  /* business cards */
  .card{width:112px;height:62px}
  .card-front-a{left:14px;top:120px}
  .card-front-b{left:140px;top:120px}
  .card-back-white{left:14px;top:212px}
  .card-back-blue{left:140px;top:212px}
  .card .edge{position:absolute;left:0;top:0;bottom:0;width:18px;border-radius:0 60% 60% 0 / 0 50% 50% 0}
  .card .card-mark{position:absolute;left:26px;top:8px;font-size:6.5px}
  .card .card-mark .dot{width:7px;height:7px;margin-right:2px}
  .card .details{position:absolute;left:26px;top:32px}
  .card-back-white .dot.big{position:absolute;left:10px;top:16px;width:30px;height:30px;background:radial-gradient(circle at 35% 35%,var(--blue-light),var(--navy))}
  .card-back-white .details{position:absolute;left:46px;top:23px}
  .card-back-blue .faint-mark{right:-10px;top:-6px;width:70px;height:70px;background:rgba(255,255,255,.12)}
  .card-back-blue .wordmark{position:absolute;left:0;width:100%;text-align:center;top:26px;font-size:9px;color:#ffffff}

  /* letterheads */
  .letterhead{top:19px;width:185px;height:282px}
  .letterhead-one{left:268px}
  .letterhead-two{left:480px}
  .letterhead .band{position:absolute;left:0;top:0;bottom:0;width:12px}
  .letterhead .faint-mark{left:60px;top:120px;width:110px;height:110px}
  .letterhead .head{position:absolute;left:22px;top:12px;font-size:7px}
  .letterhead .head .dot{width:9px;height:9px;margin-right:3px}
  .letterhead .address{position:absolute;left:96px;top:12px}
  .letterhead .footer{position:absolute;left:22px;bottom:8px}

  /* envelopes */
  .envelope{width:205px;height:100px}
  .env-front-a{left:712px;top:62px}
  .env-back-a{left:946px;top:62px;width:222px}
  .env-front-b{left:712px;top:190px}
  .env-back-b{left:946px;top:190px;width:222px}
  .envelope .band{position:absolute;left:0;top:0;bottom:0;width:10px}
  .envelope .env-mark{position:absolute;left:18px;top:9px;font-size:6.5px}
  .envelope .env-mark .dot{width:8px;height:8px;margin-right:2px}
  .envelope .return{position:absolute;left:18px;top:22px}
  .envelope .flap{position:absolute;left:0;top:0;width:100%;height:60%}
  .env-back-b .center-mark{position:absolute;left:50%;top:34px;transform:translateX(-50%);font-size:5px}
  .env-back-b .center-mark .dot{width:5px;height:5px;margin-right:2px}
  .env-back-a .url{position:absolute;right:10px;bottom:8px}
</style>
</head>
<body>

  <section class="brand-block">
    <span class="dot" aria-hidden="true"></span>
    <span class="wordmark">ELMCREST</span>
    <span class="tagline">TUTORING AND TEST PREP</span>
    <span class="concept">Preferred Concept</span>
  </section>

  <!-- business cards -->
  <article class="piece card card-front-a">
    <div class="clip">
      <div class="edge blue-fill"></div>
      <div class="wordmark card-mark"><span class="dot"></span>ELMCREST</div>
      <div class="details tiny">Doreen Falk, Director<br>609-555-0148<br>dfalk@elmcresttutors.com</div>
    </div>
    <span class="caption">Card Front</span>
  </article>

  <article class="piece card card-front-b">
    <div class="clip">
      <div class="edge blue-fill"></div>
      <div class="wordmark card-mark"><span class="dot"></span>ELMCREST</div>
      <div class="details tiny">245 Marlowe Park Rd, 3-B<br>Fairlow, NJ 08921<br>www.elmcresttutors.com</div>
    </div>
    <span class="caption">Card Front Alt</span>
  </article>

  <article class="piece card card-back-white">
    <div class="clip">
      <span class="dot big" aria-hidden="true"></span>
      <div class="details tiny">Entrance Exam Prep<br>Academic Tutoring<br>College Counseling</div>
    </div>
    <span class="caption">Card Back</span>
  </article>

  <article class="piece card card-back-blue blue-fill">
    <div class="clip">
      <div class="faint-mark"></div>
      <div class="wordmark">ELMCREST</div>
    </div>
    <span class="caption">Card Back Alt</span>
  </article>

  <!-- letterheads -->
  <article class="piece letterhead letterhead-one">
    <div class="clip">
      <div class="band blue-fill"></div>
      <div class="faint-mark" role="img" aria-label="Large faint brand circle"></div>
      <div class="wordmark head"><span class="dot"></span>ELMCREST</div>
      <div class="address tiny">245 Marlowe Park Rd, 3-B<br>Fairlow, NJ 08921<br>609-555-0148</div>
      <div class="footer tiny">www.elmcresttutors.com</div>
    </div>
    <span class="caption">Letterhead</span>
  </article>

  <article class="piece letterhead letterhead-two">
    <div class="clip">
      <div class="band blue-fill"></div>
      <div class="faint-mark" role="img" aria-label="Large faint brand circle"></div>
      <div class="wordmark head"><span class="dot"></span>ELMCREST</div>
      <div class="footer tiny">245 Marlowe Park Rd, 3-B &middot; Fairlow, NJ 08921 &middot; www.elmcresttutors.com</div>
    </div>
    <span class="caption">Letterhead Alt</span>
  </article>

  <!-- envelopes -->
  <article class="piece envelope env-front-a">
    <div class="clip">
      <div class="band blue-fill"></div>
      <div class="wordmark env-mark"><span class="dot"></span>ELMCREST</div>
      <div class="return tiny">245 Marlowe Park Rd, 3-B<br>Fairlow, NJ 08921</div>
    </div>
    <span class="caption">Envelope Front</span>
  </article>

  <article class="piece envelope env-back-a">
    <div class="clip">
      <svg class="flap" viewBox="0 0 222 60" preserveAspectRatio="none" aria-hidden="true">
        <defs>
          <linearGradient id="flapBlue" x1="0" y1="0" x2="1" y2="1">
            <stop offset="0" stop-color="#4a7de6"/>
            <stop offset=".5" stop-color="#1f4fc4"/>
            <stop offset="1" stop-color="#0c1f66"/>
          </linearGradient>
        </defs>
        <polygon points="0,0 222,0 111,60" fill="url(#flapBlue)"/>
      </svg>
      <div class="url tiny">www.elmcresttutors.com</div>
    </div>
    <span class="caption">Envelope Back</span>
  </article>

  <article class="piece envelope env-front-b">
    <div class="clip">
      <div class="band blue-fill"></div>
      <div class="wordmark env-mark"><span class="dot"></span>ELMCREST</div>
      <div class="return tiny">245 Marlowe Park Rd, 3-B<br>Fairlow, NJ 08921</div>
    </div>
    <span class="caption">Envelope Front Alt</span>
  </article>

  <article class="piece envelope env-back-b">
    <div class="clip">
      <svg class="flap" viewBox="0 0 222 60" preserveAspectRatio="none" aria-hidden="true">
        <polyline points="0,0 111,56 222,0" fill="none" stroke="#c9ceda" stroke-width="1"/>
      </svg>
      <div class="wordmark center-mark"><span class="dot"></span>ELMCREST</div>
    </div>
    <span class="caption">Envelope Back Alt</span>
  </article>

</body>
</html>
```